Tidewell Marketing company is looking for a web page design

Your projects should contain:

1. Header: Logo provided by us.
2. Top nav bar: offer, about us, experience, contact.
3. “Choose language” button.
4. Main section: panoramic picture (static, professional, modern).
5. Below section: 3 blocks (image+title+description), which represent our 3 main activities (titles):
• Market Research,
• Marketing Plans,
• Marketing Project.
6. ‘Contact us’ form – Message (text: “Write your message and give us details about your company and activities”), Email, SEND).
7. Page footer: (4 section: Contact, Social Media, Blog, Partners).
Updates

Hello!

I uploaded new file 'general_look', which is our idea how the page should generally look like.

BUT! it doesn't mean that your projects should look exactly like this project e.g.:
* titles Market Research, Marketing Plans, Marketing Project can be above these: Image 1,2,3.
* everything doesn't have to be in square and rectangle shape. You can try to manipulate with blocks and can add elipse elemnts or something similar.

We will appreciate your innovative ideas. Just wanted to give you general plan of the site and ilustrate all elements that we require.

Best Regards,
Benedek

IMPORTENT

Please remember that the main picture should be panoramic. Please do not close it in frame.

Target Market(s)

Small and middle sized companies, which would like to export their goods and services abroad and are interested in raising funds from Northgate Trade Council to expand their activities. These are rather industrial companies with low level of innovativeness. Our mission is to build image of the client’s company and increase awareness of their products to improve their competitiveness and innovativeness.

Industry/Entity Type

It Company

Requirements
Must have
• 1. Create designs of main page and subpage.
2. Subpage: Logo, Header, language button, place for article, navigation menu on the right side - below it “contact us” button , footer on the bottom. (In this section we are looking mainly for the design of the header and navigation menu).
3. The whole design should be a series of horizontal blocks.
4. Your projects should be associated with features such as: Reliability, Security, Professionalism, Openness, Uniqueness.
5. The design should be simple, fresh, readable, easy to use and should create a feeling of high quality services.
6. Possibility to change the panoramic picture (separate layer in a graphic file).
7. All pictures and blocks should be static, no movements.
8. Style of the page should be compliant with the logo design, font: Swiss.
9. Designs that we like: http://www.fernvale-studio.pl/, http://www.plumquarry.com/.
Should not have
• There shouldn’t be any distractions and not matching parts (whole design should be compact and easy to interpret and remember).

```html
<!DOCTYPE html>
<html lang="en">
<head>
<meta charset="utf-8">
<title>Tidewell Marketing</title>
<link href="https://fonts.googleapis.com/css2?family=Source+Sans+3:wght@400;600;700&display=swap" rel="stylesheet">
<style>
:root{
  --brand:#1d4f82;
  --ink:#222;
  --panel:#1f1f1f;
  --panel-edge:#2c2c2c;
  --text-light:#c9c9c9;
  --footer:#262626;
  --band:#5f8cb0;
  --btn-top:#2f79b4;
  --btn-bottom:#164c7c;
  --sky-top:#ffffff;
  --sky-mid:#d6e3ee;
  --sky-low:#94b5cf;
}
*{box-sizing:border-box;margin:0;padding:0}
html,body{width:1088px;height:1200px;overflow:hidden}
body{
  position:relative;
  font-family:"Source Sans 3",sans-serif;
  color:var(--ink);
  background:linear-gradient(to bottom,var(--sky-top) 0,var(--sky-top) 110px,var(--sky-mid) 470px,var(--sky-low) 864px);
}
.abs{position:absolute}

/* header */
.logo{left:109px;top:40px;display:flex;align-items:center;gap:10px}
.logo-mark{width:44px;height:44px;border-radius:50%;background:var(--brand)}
.logo-name{font-size:31px;font-weight:600;color:var(--brand);letter-spacing:-0.5px}

.lang{left:705px;top:15px;display:flex;align-items:center;gap:6px;font-size:12px;color:#111}
.lang-select{width:142px;height:24px;border:1px solid #555;border-radius:3px;background:#fff;position:relative;padding:3px 6px;font-size:12.5px}
.lang-select::after{content:"";position:absolute;right:1px;top:1px;width:22px;height:20px;background:#111;border-radius:0 2px 2px 0}
.lang-select svg{position:absolute;right:6px;top:6px;z-index:1}

.nav{left:467px;top:65px;display:flex;gap:1px}
.nav a{
  display:block;width:102px;height:28px;line-height:28px;text-align:center;
  font-size:11.5px;color:#9a9a9a;text-decoration:none;
  background:linear-gradient(#3a3a3a,#111);border-radius:3px;transform:skewX(-4deg);
  border:1px solid #000;
}
.nav a.active{background:linear-gradient(var(--btn-top),var(--btn-bottom));color:#fff;font-weight:600}

/* slider */
.slider{left:99px;top:116px;width:891px;height:310px;background:#0d0d0d;border-top:4px solid #222;box-shadow:0 18px 18px -10px rgba(0,0,0,.35)}
.panorama{position:absolute;left:12px;top:12px;width:866px;height:238px;
  background:linear-gradient(to bottom,#8f7cab 0%,#e58c86 45%,#c2625b 72%,#3a2c2e 88%,#6d4b4c 100%)}
.slide-arrow{position:absolute;top:116px;width:18px;height:20px;background:#111;display:flex;align-items:center;justify-content:center}
.slide-arrow.prev{left:12px}
.slide-arrow.next{right:12px}
.controls{position:absolute;right:22px;top:271px;display:flex;gap:4px;align-items:center}
.controls span{display:flex;align-items:center;justify-content:center;background:linear-gradient(#fff,#d6d6d6);border:1px solid #999}
.controls .small{width:20px;height:20px}
.controls .big{width:27px;height:27px}

/* services */
.service-img{top:466px;width:285px;height:228px;background:var(--panel);border:1px solid #444;padding:9px}
.service-img div{width:100%;height:100%}
.img-research{background:linear-gradient(135deg,#efe6dc,#b84a5a 55%,#6a6a6a)}
.img-plans{background:radial-gradient(ellipse at 45% 50%,#3b6fc4 0,#2a56a8 30%,#f0f2f6 62%,#fff 100%)}
.img-project{background:linear-gradient(120deg,#2d2d2d,#5dbdde 45%,#d7d2cc 75%,#8a8f94)}
.service-text{top:703px;width:283px;height:131px;background:linear-gradient(#2a2a2a,#1d1d1d);padding:0 8px;box-shadow:0 10px 8px -6px rgba(0,0,0,.4)}
.service-text h2{font-weight:400;font-size:18.5px;color:#fff;text-align:center;line-height:18px;padding-top:10px;padding-bottom:9px;margin:0 30px 10px;border-bottom:1px solid #4a4a4a}
.service-text p{font-size:12.5px;line-height:18px;color:var(--text-light)}

/* footer */
.footer{left:0;top:864px;width:1088px;height:258px;background:var(--footer)}
.footer h3{position:absolute;top:22px;font-size:16.5px;font-weight:600;color:#fff}
.social{position:absolute;left:109px;top:84px;display:flex;gap:8px}
.social span{width:40px;height:40px;border-radius:50%;border:2px solid #fff}
.blog-list{position:absolute;left:423px;top:62px;width:232px;list-style:none}
.blog-list li{font-size:10px;line-height:14.5px;color:#b5b5b5;text-align:justify;padding-left:12px;position:relative;margin-bottom:24px}
.blog-list li::before{content:"";position:absolute;left:2px;top:5px;width:5px;height:5px;border-radius:50%;background:#eee}
.btn{position:absolute;top:212px;height:29px;line-height:27px;text-align:center;color:#fff;font-size:13.5px;font-weight:600;
  background:linear-gradient(var(--btn-top),var(--btn-bottom));border:1px solid #0b2f50}
.message{position:absolute;left:743px;top:54px;width:237px;height:150px;background:linear-gradient(#3d3d3d,#4e4e4e);border:1px solid #6a6a6a;padding:11px 8px;font-size:13px;line-height:15px;color:#eee}
.bottom-band{left:0;top:1122px;width:1088px;height:78px;background:var(--band);font-size:16.5px;font-weight:600;color:#1a1a1a}
.bottom-band .brand{color:var(--brand)}
</style>
</head>
<body>

<header>
  <div class="abs logo"><span class="logo-mark"></span><span class="logo-name">Tidewell Marketing</span></div>
  <div class="abs lang">Choose Your language:
    <div class="lang-select">English
      <svg width="10" height="9" viewBox="0 0 10 9"><path d="M0 0h10L5 9z" fill="#fff"/></svg>
    </div>
  </div>
  <nav class="abs nav">
    <a class="active">Home</a><a>Offer</a><a>About us</a><a>Experience</a><a>Contact</a>
  </nav>
</header>

<section class="abs slider">
  <div class="panorama" role="img" aria-label="Panoramic city skyline at sunset reflected on the water"></div>
  <span class="slide-arrow prev"><svg width="6" height="8"><path d="M6 0v8L0 4z" fill="#fff"/></svg></span>
  <span class="slide-arrow next"><svg width="6" height="8"><path d="M0 0v8l6-4z" fill="#fff"/></svg></span>
  <div class="controls">
    <span class="small"><svg width="4" height="6"><path d="M4 0v6L0 3z" fill="#111"/></svg></span>
    <span class="big"><svg width="7" height="9"><path d="M0 0v9l7-4.5z" fill="#111"/></svg></span>
    <span class="small"><svg width="4" height="6"><path d="M0 0v6l4-3z" fill="#111"/></svg></span>
  </div>
</section>

<section>
  <div class="abs service-img" style="left:108px"><div class="img-research" role="img" aria-label="Magnifying glass over a bar chart"></div></div>
  <div class="abs service-img" style="left:403px"><div class="img-plans" role="img" aria-label="Globe shaped as a pie chart with an orange slice"></div></div>
  <div class="abs service-img" style="left:696px"><div class="img-project" role="img" aria-label="Bus stop with advertising posters on a city street"></div></div>

  <article class="abs service-text" style="left:109px">
    <h2>Market Research</h2>
    <p>Lorem Ipsum is simply dummy text of the printing and typesetting industry. Lorem Ipsum has been the industry's standard dummy text ever since the 1500s</p>
  </article>
  <article class="abs service-text" style="left:404px">
    <h2>Marketing Plans</h2>
    <p>Lorem Ipsum is simply dummy text of the printing and typesetting industry. Lorem Ipsum has been the industry's standard dummy text ever since the 1500s</p>
  </article>
  <article class="abs service-text" style="left:698px">
    <h2>Marketing Project</h2>
    <p>Lorem Ipsum is simply dummy text of the printing and typesetting industry. Lorem Ipsum has been the industry's standard dummy text ever since the 1500s</p>
  </article>
</section>

<footer class="abs footer">
  <h3 style="left:109px">Follow us</h3>
  <div class="social">
    <span style="background:#1f4f9a"></span>
    <span style="background:#1b7fa8"></span>
    <span style="background:#3aa6e0"></span>
    <span style="background:#f07d24"></span>
  </div>

  <h3 style="left:424px">Blogs</h3>
  <ul class="blog-list">
    <li>Lorem Ipsum is simply dummy text of the printing and typesetting industry. Lorem Ipsum has been the industry's s</li>
    <li>Lorem Ipsum is simply dummy text of the printing and typesetting industry. Lorem Ipsum has been the industry's s</li>
  </ul>
  <div class="btn" style="left:568px;width:93px">See More</div>

  <h3 style="left:743px">Contact us</h3>
  <div class="message">Write your message and give us details about your company and activities</div>
  <div class="btn" style="left:888px;width:92px">Send</div>
</footer>

<div class="abs bottom-band">
  <div class="abs" style="left:109px;top:16px"><span class="brand">Tidewell</span> marketing © 2012 All rights reserved.</div>
  <div class="abs" style="right:108px;top:16px">Created by: <span class="brand">Tidewell</span> marketing</div>
</div>

</body>
</html>
```